Logo, homepage, and product page design cleaning equipment

Looking for a logo, homepage, and product page design for our cartwell store. We sell cleaning equipment that serves the auto detailing industry. I have attached a picture of our main product. The company is called Brisk Cleaning Equipment with a slogan of The Way to Clean (slogan incorporated is optional). A site I really like is https://www.harborlanternroast.example/. It has a very clean layout and very clear on their messaging.

Target Market(s)

Auto detailing industry

Industry/Entity Type

Automotive

Logo Text

Brisk Cleaning Equipment

Font styles to use
Serif
Sans Serif

Requirements
Must have
• A nice clean layout. Not too busy. Easy to navigate.
Nice to have
• consistency in colors. Appeal to people who care about their cars. They have an eye for detail.
Should not have
• It cannot be too busy.

```html
<!DOCTYPE html>
<html lang="en">
<head>
<meta charset="utf-8">
<title>Brisk Cleaning Equipment</title>
<link href="https://fonts.googleapis.com/css2?family=Alfa+Slab+One&family=Jost:wght@400;500;600;700&family=Mulish:wght@400;600;700&display=swap" rel="stylesheet">
<style>
:root{
  --ink:#111;
  --red:#f01111;
  --navy:#1d2a6b;
  --hero:#f0f1f3;
  --muted:#666;
  --line:#e4e4e4;
  --footer:#232323;
  --footer-base:#1a1a1a;
  --field:#7a7a7a;
  --link:#3b5bdb;
}
*{box-sizing:border-box;margin:0;padding:0}
html,body{width:688px;height:1200px;overflow:hidden;background:#fff}
body{position:relative;font-family:"Mulish",sans-serif;color:var(--ink)}
.abs{position:absolute}

/* header */
.site-header{left:0;top:0;width:688px;height:74px;background:#fff}
.nav-link{font-family:"Mulish",sans-serif;font-size:7px;letter-spacing:.5px;text-transform:uppercase;color:#222;top:46px}
.account{top:12px;left:481px;font-size:7px;color:#222;display:flex;align-items:center;gap:6px}
.account svg{display:block}
.cart-count{position:absolute;left:96px;top:-3px;width:7px;height:7px;border-radius:50%;background:var(--red);color:#fff;font-size:5px;line-height:7px;text-align:center}
.brand{left:301px;top:5px;width:86px;height:86px;border-radius:50%;background:#fff;border:3px solid var(--navy);display:flex;align-items:center;justify-content:center;text-align:center;z-index:2}
.brand-name{font-family:"Mulish",sans-serif;font-weight:700;font-size:9px;line-height:11px;color:var(--navy);text-transform:uppercase}

/* hero */
.hero{left:0;top:74px;width:688px;height:276px;background:var(--hero)}
.hero-product{left:200px;top:88px;width:140px;height:248px;border-radius:40px 40px 10px 10px;background:linear-gradient(90deg,#1a1a1a,#3a3a3a 60%,#1a1a1a)}
.hero-kicker{left:387px;top:131px;font-family:"Jost",sans-serif;font-size:18px;color:#111}
.hero-title{left:384px;top:148px;font-family:"Alfa Slab One",serif;font-size:44px;line-height:56px;letter-spacing:1px;color:var(--red)}
.hero-copy{left:394px;top:204px;width:194px;font-size:9px;line-height:13px;color:#333}
.btn-dark{left:395px;top:253px;width:71px;height:30px;background:#000;color:#fff;font-size:9px;font-weight:700;display:flex;align-items:center;justify-content:center}

/* section headings */
.section-title{left:0;width:688px;text-align:center;font-family:"Jost",sans-serif;font-weight:600;font-size:29px;letter-spacing:1px}

/* products */
.product-card{top:455px;width:238px;height:163px;border:1px solid var(--line);background:#fff}
.product-shot{position:absolute;left:86px;top:28px;width:64px;height:108px;border-radius:18px 18px 6px 6px;background:linear-gradient(90deg,#1c1c1c,#3b3b3b 60%,#1c1c1c)}
.product-name{top:634px;width:238px;text-align:center;font-family:"Jost",sans-serif;font-size:12.5px;letter-spacing:.4px}
.btn-red{top:658px;width:66px;height:22px;background:var(--red);color:#fff;font-size:9px;font-weight:600;display:flex;align-items:center;justify-content:center}
.carousel-arrow{top:527px;width:19px;height:19px;background:#000;display:flex;align-items:center;justify-content:center}

/* blog */
.post{top:806px;width:156px}
.post-photo{width:156px;height:100px}
.post-title{margin-top:10px;font-family:"Jost",sans-serif;font-weight:600;font-size:10.5px;line-height:13px}
.post-meta{margin-top:10px;font-size:7px;color:var(--muted);display:flex;gap:12px;align-items:center}
.post-meta span{display:flex;align-items:center;gap:5px}
.post-excerpt{margin-top:6px;font-size:7px;line-height:11px;color:var(--muted)}

/* footer */
.site-footer{left:0;top:1033px;width:688px;height:139px;background:var(--footer)}
.footer-links{font-size:7.5px;line-height:14px;color:#fff;list-style:none}
.newsletter-title{left:309px;top:1064px;font-family:"Jost",sans-serif;font-weight:600;font-size:10.5px;letter-spacing:1.5px;color:#fff}
.newsletter-copy{left:309px;top:1088px;font-size:7.5px;color:#fff}
.newsletter-field{left:309px;top:1107px;width:196px;height:18px;background:var(--field);color:#ddd;font-size:7.5px;padding-left:7px;line-height:18px}
.newsletter-btn{left:309px;top:1130px;width:196px;height:18px;background:var(--red);color:#fff;font-size:9px;font-weight:700;text-align:center;line-height:18px}
.social-dot{top:1148px;width:8px;height:8px;border-radius:50%;background:#fff}
.copyright-bar{left:0;top:1172px;width:688px;height:28px;background:var(--footer-base)}
.copyright{left:143px;top:1182px;font-size:7px;color:#fff}
</style>
</head>
<body>

<header class="site-header abs">
  <nav>
    <span class="nav-link abs" style="left:197px">About</span>
    <span class="nav-link abs" style="left:251px">Shop</span>
    <span class="nav-link abs" style="left:416px">Blog</span>
    <span class="nav-link abs" style="left:463px">Contact Us</span>
  </nav>
  <div class="account abs">
    <svg width="7" height="8" viewBox="0 0 7 8"><circle cx="3.5" cy="2" r="2" fill="#777"/><path d="M0 8c0-3 7-3 7 0z" fill="#777"/></svg>
    <span>Login / Sign up</span>
    <svg width="8" height="8" viewBox="0 0 8 8" style="margin-left:10px"><circle cx="3.2" cy="3.2" r="2.4" fill="none" stroke="#444" stroke-width="1.2"/><path d="M5 5l2.5 2.5" stroke="#444" stroke-width="1.3"/></svg>
    <svg width="9" height="8" viewBox="0 0 9 8" style="margin-left:2px"><path d="M0 1h2l1 4h5l1-3H2.5" fill="none" stroke="#444" stroke-width="1"/><circle cx="3.5" cy="7" r=".9" fill="#444"/><circle cx="7" cy="7" r=".9" fill="#444"/></svg>
    <span class="cart-count">0</span>
  </div>
</header>

<div class="brand abs"><span class="brand-name">Brisk<br>Cleaning<br>Equipment</span></div>

<section class="hero abs"></section>
<div class="hero-product abs" role="img" aria-label="Black pump foam sprayer bottle with blue trigger"></div>
<p class="hero-kicker abs">The Way to</p>
<h1 class="hero-title abs">CLEAN</h1>
<p class="hero-copy abs">Excepteur sint occaecat cupidatat non proident sunt in culpa qui officia deserunt mollit anim id est laborum</p>
<a class="btn-dark abs">Buy Now</a>

<h2 class="section-title abs" style="top:392px">OTHER PRODUCTS</h2>

<div class="carousel-arrow abs" style="left:61px"><svg width="6" height="8" viewBox="0 0 6 8"><path d="M4.5 1L1.5 4l3 3" fill="none" stroke="#fff" stroke-width="1.5"/></svg></div>
<div class="carousel-arrow abs" style="left:603px"><svg width="6" height="8" viewBox="0 0 6 8"><path d="M1.5 1l3 3-3 3" fill="none" stroke="#fff" stroke-width="1.5"/></svg></div>

<div class="product-card abs" style="left:99px"><div class="product-shot" role="img" aria-label="Black pump foam sprayer bottle"></div></div>
<p class="product-name abs" style="left:99px">Dolorem eum fugiat quo</p>
<a class="btn-red abs" style="left:185px">Buy Now</a>

<div class="product-card abs" style="left:351px"><div class="product-shot" role="img" aria-label="Black pump foam sprayer bottle"></div></div>
<p class="product-name abs" style="left:351px">Dolorem eum fugiat quo</p>
<a class="btn-red abs" style="left:437px">Buy Now</a>

<h2 class="section-title abs" style="top:731px">BLOG</h2>

<article class="post abs" style="left:99px">
  <div class="post-photo" role="img" aria-label="Detailer foaming a car with a sprayer" style="background:linear-gradient(135deg,#6b6a66,#c9ccd0 55%,#8e9196)"></div>
  <h3 class="post-title">Nam libero tempore cum soluta nobis est eligendi</h3>
  <div class="post-meta"><span><svg width="6" height="6" viewBox="0 0 7 8"><circle cx="3.5" cy="2" r="2" fill="#999"/><path d="M0 8c0-3 7-3 7 0z" fill="#999"/></svg>Admin</span><span><svg width="6" height="6" viewBox="0 0 6 6"><rect x=".5" y="1" width="5" height="4.5" fill="none" stroke="#999"/></svg>12th Sept 2018</span></div>
  <p class="post-excerpt">Omnis voluptas assumenda est, omnis dolor repellendus. Temporibus autem quibusdam officiis debitis aut rerum necessitatibus</p>
</article>

<article class="post abs" style="left:267px">
  <div class="post-photo" role="img" aria-label="Hand wiping a black car hood with a microfiber cloth" style="background:linear-gradient(135deg,#2a2a2a,#5b5e62 50%,#1e1e1e)"></div>
  <h3 class="post-title">Nam libero tempore cum soluta nobis est eligendi</h3>
  <div class="post-meta"><span><svg width="6" height="6" viewBox="0 0 7 8"><circle cx="3.5" cy="2" r="2" fill="#999"/><path d="M0 8c0-3 7-3 7 0z" fill="#999"/></svg>Admin</span><span><svg width="6" height="6" viewBox="0 0 6 6"><rect x=".5" y="1" width="5" height="4.5" fill="none" stroke="#999"/></svg>12th Sept 2018</span></div>
  <p class="post-excerpt">Omnis voluptas assumenda est, omnis dolor repellendus. Temporibus autem quibusdam officiis debitis aut rerum necessitatibus</p>
</article>

<article class="post abs" style="left:435px">
  <div class="post-photo" role="img" aria-label="Person washing the front of a dark car with soap" style="background:linear-gradient(135deg,#8a7f74,#3a3d44 55%,#b7b2aa)"></div>
  <h3 class="post-title">Nam libero tempore cum soluta nobis est eligendi</h3>
  <div class="post-meta"><span><svg width="6" height="6" viewBox="0 0 7 8"><circle cx="3.5" cy="2" r="2" fill="#999"/><path d="M0 8c0-3 7-3 7 0z" fill="#999"/></svg>Admin</span><span><svg width="6" height="6" viewBox="0 0 6 6"><rect x=".5" y="1" width="5" height="4.5" fill="none" stroke="#999"/></svg>12th Sept 2018</span></div>
  <p class="post-excerpt">Omnis voluptas assumenda est, omnis dolor repellendus. Temporibus autem quibusdam officiis debitis aut rerum necessitatibus</p>
</article>

<footer class="site-footer abs"></footer>
<ul class="footer-links abs" style="left:139px;top:1071px"><li>About</li><li>Shop</li><li>Blog</li><li>Contact Us</li></ul>
<ul class="footer-links abs" style="left:183px;top:1071px"><li>Terms and Conditions</li><li>Shipping Details</li></ul>
<span class="social-dot abs" style="left:149px"></span>
<span class="social-dot abs" style="left:166px"></span>
<span class="social-dot abs" style="left:187px"></span>
<h4 class="newsletter-title abs">NEWSLETTER</h4>
<p class="newsletter-copy abs">Subscribe to our newsletter for latest updates</p>
<div class="newsletter-field abs">Email</div>
<div class="newsletter-btn abs">Subscribe</div>
<div class="copyright-bar abs"></div>
<p class="copyright abs">©Copyright information here</p>

</body>
</html>
```